Redesign Event Flyer for Speaker

We are re-designing our professional event flyer template with new headshot and cleaner, up-to-date design. All design details are in PDF file attached. Thank you for participating :)

Font styles to use
Sans Serif

Colors
3276b5
0355a3

Requirements
Must have
• All elements in PDF file.
Nice to have
Should not have
• Tacky or childish elements.

```html
<!DOCTYPE html>
<html lang="en">
<head>
<meta charset="utf-8">
<title>The Greatest Sale – Speaker Event Flyer</title>
<link href="https://fonts.googleapis.com/css2?family=Bebas+Neue&family=Cinzel:wght@600&family=Oswald:wght@300;400&display=swap" rel="stylesheet">
<style>
  :root {
    --blue-deep: #0355a3;
    --blue-mid: #3276b5;
    --blue-glow: #1e6cbc;
    --circle-light: #8fb8e2;
    --white: #ffffff;
    --photo-light: #6b6f78;
    --photo-dark: #121317;
  }
  * { margin: 0; padding: 0; box-sizing: border-box; }
  html, body { width: 1200px; height: 848px; overflow: hidden; background: var(--blue-deep); }
  .flyer {
    position: relative;
    width: 1200px;
    height: 848px;
    overflow: hidden;
    background: radial-gradient(ellipse 60% 65% at 55% 40%, var(--blue-glow) 0%, var(--blue-deep) 100%);
    color: var(--white);
  }
  .backdrop, .typography { position: absolute; inset: 0; width: 1200px; height: 848px; }
  .speaker-photo { position: absolute; left: 298px; top: 42px; }
  .brand {
    position: absolute;
    right: 66px;
    top: 66px;
    display: flex;
    align-items: center;
    gap: 12px;
    font-family: "Oswald", sans-serif;
    font-weight: 400;
    font-size: 40px;
    line-height: 1;
    letter-spacing: 0.5px;
  }
  .brand-dot { width: 30px; height: 30px; border-radius: 50%; background: var(--white); }
  .headline-text { font-family: "Bebas Neue", sans-serif; font-size: 174px; fill: var(--white); }
  .headline-outline { fill: none; stroke: var(--white); stroke-width: 2.2; }
  .speaker-name { font-family: "Cinzel", serif; font-weight: 600; font-size: 20px; fill: var(--white); }
  .detail-text { font-family: "Oswald", sans-serif; font-weight: 300; font-size: 19px; fill: var(--white); }
  .icon { fill: none; stroke: var(--white); }
  .divider { stroke: var(--white); stroke-width: 1.5; }
</style>
</head>
<body>
<main class="flyer">
  <svg class="backdrop" viewBox="0 0 1200 848" aria-hidden="true">
    <defs>
      <linearGradient id="circleFront" x1="0" y1="0" x2="1" y2="0">
        <stop offset="0" stop-color="#7fb0e0"/>
        <stop offset="0.55" stop-color="#dbe8f6"/>
        <stop offset="1" stop-color="#ffffff"/>
      </linearGradient>
    </defs>
    <circle cx="367" cy="465" r="213" fill="var(--circle-light)" opacity="0.55"/>
    <circle cx="617" cy="430" r="250" fill="url(#circleFront)" opacity="0.95"/>
  </svg>

  <svg class="speaker-photo" width="670" height="806" viewBox="0 0 670 806" role="img" aria-label="Black and white headshot of the speaker in a dark suit jacket and white open-collar shirt">
    <defs>
      <linearGradient id="photoTone" x1="0" y1="0" x2="0" y2="1">
        <stop offset="0" stop-color="var(--photo-light)"/>
        <stop offset="0.45" stop-color="#2b2d33"/>
        <stop offset="1" stop-color="var(--photo-dark)"/>
      </linearGradient>
    </defs>
    <path d="M300 0 Q390 0 396 90 Q400 200 380 250 L384 290 Q480 320 540 360 Q600 400 640 560 L670 806 H0 L30 560 Q60 400 120 360 Q180 320 250 290 L252 250 Q226 200 224 90 Q228 0 300 0 Z" fill="url(#photoTone)"/>
  </svg>

  <div class="brand"><span class="brand-dot"></span><span>Signovar</span></div>

  <svg class="typography" viewBox="0 0 1200 848">
    <text class="headline-text" x="212" y="576" textLength="190" lengthAdjust="spacingAndGlyphs">THE</text>
    <text class="headline-text" x="214" y="710" textLength="500" lengthAdjust="spacingAndGlyphs">GREATEST</text>
    <text class="headline-text headline-outline" x="744" y="710" textLength="244" lengthAdjust="spacingAndGlyphs">SALE</text>

    <text class="speaker-name" x="223" y="744" textLength="325" lengthAdjust="spacing">MARCUS DANIEL AVERY</text>

    <g class="event-details">
      <g class="icon" stroke-width="2" transform="translate(66 786)">
        <path d="M13 36 C5 24 2 18 2 13 A11 11 0 0 1 24 13 C24 18 21 24 13 36 Z"/>
        <circle cx="13" cy="13" r="4.5"/>
      </g>
      <text class="detail-text" x="112" y="792" textLength="200" lengthAdjust="spacingAndGlyphs">ROLLING FALLS GOLF CLUB</text>
      <text class="detail-text" x="112" y="813" textLength="338" lengthAdjust="spacingAndGlyphs">4200 RIVERSIDE PKWY, LAKEVIEW FALLS, CANADA</text>

      <line class="divider" x1="468" y1="792" x2="468" y2="820"/>

      <g class="icon" transform="translate(491 793)">
        <rect x="1" y="3" width="24" height="20" stroke-width="1.8"/>
        <line x1="1" y1="8" x2="25" y2="8" stroke-width="1.8"/>
        <line x1="7" y1="0" x2="7" y2="5" stroke-width="1.8"/>
        <line x1="19" y1="0" x2="19" y2="5" stroke-width="1.8"/>
        <path d="M5 12h16M5 16h16M5 20h16M9 10v12M13 10v12M17 10v12" stroke-width="1"/>
      </g>
      <text class="detail-text" x="537" y="813" textLength="172" lengthAdjust="spacingAndGlyphs">FRIDAY, AUGUST 9TH, 2019</text>

      <line class="divider" x1="732" y1="792" x2="732" y2="820"/>

      <g class="icon" transform="translate(755 792)">
        <circle cx="14" cy="14" r="12.5" stroke-width="1.8"/>
        <ellipse cx="14" cy="14" rx="5.5" ry="12.5" stroke-width="1.5"/>
        <path d="M1.5 14h25M3.5 7.5h21M3.5 20.5h21" stroke-width="1.5"/>
      </g>
      <text class="detail-text" x="803" y="813" textLength="333" lengthAdjust="spacingAndGlyphs">MARCUSDANIELAVERY.COM | SIGNOVAR.CA</text>
    </g>
  </svg>
</main>
</body>
</html>
```